Retail Jewelry Business Card Design Project

We are in need of a new business card design for a retail jewelry store. This store is in the business of fine jewelry including but not specific to bridal jewelry, diamonds, designer jewelry and watches.

This store has been in business for 20 years but continues to strive for a modern professional appeal. The main colors use for this business are a royal blue, white and silver.

Target Market(s)

Target market is ages 18-50

Industry/Entity Type

Jewelry

Requirements
Must have
• Sales Person Name
Sales Person Email Address

Store Address
Store Phone
Website

Standard business card size. No odd shapes or sizes.
Nice to have
• Overall modern feel for card.

We have thought that a design with a nice feature of the logo on the back of the card would be nice but open to ideas.
Should not have
• No specific images of jewelry should be used.

```html
<!DOCTYPE html>
<html lang="en">
<head>
<meta charset="utf-8">
<title>Marlowe Grant Fine Jewelry – Business Cards</title>
<link rel="stylesheet" href="https://fonts.googleapis.com/css2?family=Tinos&display=swap">
<style>
  :root {
    --backdrop: #3a3531;
    --royal-navy: #2b2762;
    --royal-navy-deep: #221f52;
    --silver: #dcdde4;
    --silver-soft: #bfc1ce;
  }
  * { margin: 0; padding: 0; box-sizing: border-box; }
  html, body {
    width: 1200px;
    height: 802px;
    overflow: hidden;
    background: var(--backdrop);
  }
  .canvas {
    width: 1200px;
    height: 802px;
    display: flex;
    align-items: center;
    justify-content: center;
    gap: 80px;
    font-family: "Tinos", serif;
  }
  .card {
    position: relative;
    width: 500px;
    height: 286px;
    border-radius: 8px;
    background: linear-gradient(160deg, var(--royal-navy) 0%, var(--royal-navy-deep) 100%);
    box-shadow: 0 18px 40px rgba(0, 0, 0, 0.45);
    overflow: hidden;
  }
  .brand-name {
    font-family: "Tinos", serif;
    font-weight: 400;
    color: var(--silver);
    letter-spacing: 0.5px;
    white-space: nowrap;
  }
  .brand-rule {
    height: 1px;
    background: var(--silver-soft);
    margin-top: 6px;
  }

  /* Front: contact details */
  .card-front { padding: 28px 34px; }
  .card-front .brand { display: inline-block; }
  .card-front .brand-name { font-size: 20px; }
  .contact {
    margin-top: 18px;
    color: var(--silver-soft);
    font-size: 13px;
    line-height: 1.45;
  }
  .contact .person { font-size: 16px; color: var(--silver); }
  .contact .email { margin-bottom: 12px; }
  .contact .address { margin-bottom: 8px; }

  /* Back: brand */
  .card-back {
    display: flex;
    flex-direction: column;
    align-items: center;
    justify-content: center;
    text-align: center;
  }
  .card-back .brand { display: inline-block; }
  .card-back .brand-name { font-size: 30px; }
  .card-back .website,
  .card-back .phone {
    font-size: 16px;
    letter-spacing: 0.6px;
    color: var(--silver-soft);
  }
  .card-back .website { margin-top: 16px; }
  .card-back .phone { margin-top: 6px; font-size: 14px; }
</style>
</head>
<body>
  <main class="canvas">
    <section class="card card-front" aria-label="Card front">
      <div class="brand">
        <div class="brand-name">Marlowe Grant Fine Jewelry</div>
        <div class="brand-rule"></div>
      </div>
      <div class="contact">
        <div class="person">Marlowe Grant Ellison</div>
        <div class="email">marlowe@marlowegrantjewelry.com</div>
        <div class="address">Marlowe Grant Fine Jewelry<br>2280 Linden Avenue<br>Harbor Bend, FL 32410</div>
        <div class="phone">(850) 555-0147</div>
        <div class="web">www.marlowegrantjewelry.com</div>
      </div>
    </section>

    <section class="card card-back" aria-label="Card back">
      <div class="brand">
        <div class="brand-name">Marlowe Grant Fine Jewelry</div>
        <div class="brand-rule"></div>
      </div>
      <div class="website">www.marlowegrantjewelry.com</div>
      <div class="phone">(850) 555-0147</div>
    </section>
  </main>
</body>
</html>
```